Beautiful design for wordpress

I need a beautiful, colourful and feminine website. My business is called 'The Velvet Lantern', and I sell crystals, books, CD's, pendulums and other metaphysical items. I also provide Reiki (energy healing).
I want this design to be eye catching and inspire happiness and joy in those who see it. And I would love to see the use of the logo and its colours :)
Please add these on the web design: Home, About, Online store, Blog

Must have
• Colourful and playful, must use the logo somewhere, have the words on a menu saying 'Home, Blog, Online store and about' (or similar to those)And the design must stand out!
Should not have
• grey, brown and other boring colours.

```html
<!DOCTYPE html>
<html lang="en">
<head>
<meta charset="utf-8">
<title>The Velvet Lantern — Crystals &amp; Gifts</title>
<link rel="stylesheet" href="https://fonts.googleapis.com/css2?family=Cabin:wght@400;500;600;700&display=swap">
<style>
:root{
  --pink:#f2508c;
  --pink-soft:#f592c2;
  --coral:#e8605b;
  --green:#a8c94c;
  --orange:#f7a46c;
  --nav:#5a5a5a;
  --text:#444;
  --muted:#888;
  --line:#dcdcdc;
  --panel:#f3f3f3;
  --footer:#efefef;
  --white:#fff;
}
*{box-sizing:border-box;margin:0;padding:0}
html,body{width:900px;height:1200px;overflow:hidden;background:var(--white)}
body{font-family:"Cabin",sans-serif;color:var(--text);position:relative}
.abs{position:absolute}

/* header */
.brand{left:75px;top:40px;width:150px;display:flex;align-items:center;gap:8px}
.brand-dot{width:22px;height:22px;border-radius:50%;background:var(--green);flex:none}
.brand-name{font-size:24px;font-weight:700;color:var(--nav);line-height:1.05}
.brand-tag{left:110px;top:148px;font-size:8px;letter-spacing:2px;color:var(--nav)}
.phone{left:552px;top:9px;font-size:15px;letter-spacing:1px;color:var(--nav);display:flex;align-items:center;gap:7px}
.cart{left:680px;top:0;width:145px;height:33px;background:var(--orange);display:flex;align-items:center;color:#fff;font-size:11px}
.cart-icon{width:38px;height:33px;display:flex;align-items:center;justify-content:center;background:#f9b88a}
.cart span{padding-left:9px}
.perks{left:408px;top:68px;display:flex;gap:0}
.perk{display:flex;align-items:center;gap:8px;padding:0 13px;font-size:10.5px;line-height:1.15;color:#9a9a9a;border-right:1px solid var(--line);height:34px}
.perk:last-child{border-right:0}
.perk:first-child{padding-left:0}

/* navigation */
.nav{left:225px;top:127px;width:600px;height:31px;background:var(--nav);display:flex}
.nav-home{width:37px;background:var(--green);display:flex;align-items:center;justify-content:center}
.nav a{color:#fff;text-decoration:none;font-size:11px;letter-spacing:.6px;line-height:31px;padding:0 17px}
.nav-search{margin-left:auto;width:210px;background:var(--pink-soft);display:flex;align-items:center;border-right:3px solid var(--pink)}
.nav-search .ico{width:33px;height:31px;background:var(--pink);display:flex;align-items:center;justify-content:center}
.nav-search span{color:#fff;font-size:9px;padding-left:13px}

/* hero */
.hero{left:75px;top:172px;width:750px;height:281px}
.hero-bg{position:absolute;inset:0;background:radial-gradient(circle at 70% 10%,#f7e7c8 0,transparent 25%),radial-gradient(circle at 85% 45%,#f3d6dc 0,transparent 18%),linear-gradient(#f4f4f4,#ececec 45%,#dedede 70%,#ececec)}
.hero-title{position:absolute;top:114px;width:100%;text-align:center;font-size:38px;font-weight:600;letter-spacing:3px;color:var(--coral)}
.hero-sub{position:absolute;top:167px;width:100%;text-align:center;font-size:16.5px;letter-spacing:1.5px;color:#555}
.hero-arrow{position:absolute;top:120px;width:45px;height:46px;background:#f4f4f4;display:flex;align-items:center;justify-content:center}

/* promo */
.promo{top:465px;width:367px;height:149px;background:var(--panel)}
.promo-kicker{position:absolute;left:12px;top:11px;font-size:7px;letter-spacing:.6px;color:#555}
.promo-big{position:absolute;left:13px;top:19px;font-size:19px;line-height:.85;color:var(--coral);letter-spacing:1px}
.promo-img{position:absolute;top:17px;height:120px}
.promo-info{position:absolute;left:257px;top:28px}
.promo-name{font-size:13.5px;line-height:1.2;color:#555}
.price{font-size:14px;font-weight:600;color:var(--green)}
.old{font-size:10px;color:var(--coral);text-decoration:line-through}
.btn{display:inline-block;background:var(--pink);color:#fff;font-size:9.5px;font-weight:700;letter-spacing:.6px;padding:4px 8px}

/* products */
.sec-title{left:75px;top:632px;font-size:11px;letter-spacing:1.2px;font-weight:500;color:#333}
.sec-rule{left:75px;top:651px;width:750px;height:1px;background:#e6e6e6}
.card{top:666px;width:151px;height:211px;text-align:center}
.card.active{box-shadow:0 0 3px rgba(0,0,0,.2)}
.badge{position:absolute;left:7px;top:8px;background:var(--coral);color:#fff;font-size:7px;padding:2px 5px}
.thumb{position:absolute;left:24px;top:22px;width:103px;height:106px}
.card-name{position:absolute;top:132px;width:100%;font-size:13px;color:#444}
.card .price{position:absolute;top:154px;width:100%}
.card .btn{position:absolute;top:177px;left:50%;transform:translateX(-50%);white-space:nowrap}
.slide-arrow{top:745px}

/* footer */
.footer{left:0;top:907px;width:900px;height:250px;background:var(--footer)}
.f-col{top:940px;width:236px}
.f-head{font-size:11px;letter-spacing:1px;color:#444;padding-bottom:9px;border-bottom:1px solid var(--line)}
.f-list{list-style:none}
.f-list li{font-size:10.5px;color:#666;padding:9px 0 8px 2px;border-bottom:1px solid var(--line)}
.f-list li.current{color:#222;padding-left:5px}
.info{font-size:10.5px;color:#555;line-height:1.6}
.info-row{display:flex;gap:8px;margin-top:9px}
.social{display:flex;gap:9px;margin-top:11px}
.social span{width:24px;height:24px;border-radius:50%;background:#6a6a6a}
.mail{margin-top:8px;width:236px;height:23px;background:#fff;border:1px solid var(--line);font-size:10px;color:#aaa;display:flex;align-items:center;justify-content:space-between;padding:0 7px}
.mail-note{font-size:8.5px;color:#666;margin-top:8px;line-height:1.25}
.copy{left:75px;top:1172px;font-size:10.5px;color:#555}
.copy b{font-weight:600}
.pay{left:553px;top:1166px;display:flex;gap:8px}
.pay span{width:37px;height:23px;border:1px solid #ddd;border-radius:2px}
</style>
</head>
<body>

<!-- header -->
<div class="abs brand"><span class="brand-dot"></span><span class="brand-name">The Velvet Lantern</span></div>
<div class="abs brand-tag">CRYSTALS &amp; GIFTS</div>

<div class="abs phone">
  <svg width="9" height="14" viewBox="0 0 9 14"><rect x="1" y="1" width="7" height="12" rx="1.5" fill="none" stroke="#5a5a5a" stroke-width="1.5"/><line x1="3" y1="11" x2="6" y2="11" stroke="#5a5a5a"/></svg>
  00 0000 000
</div>
<div class="abs cart">
  <div class="cart-icon"><svg width="20" height="16" viewBox="0 0 20 16"><path d="M1 2h3l2 9h10l2-7H6" fill="none" stroke="#fff" stroke-width="1.6"/><circle cx="8" cy="14" r="1.4" fill="#fff"/><circle cx="15" cy="14" r="1.4" fill="#fff"/></svg></div>
  <span>0 items – $0.00 ▾</span>
</div>

<div class="abs perks">
  <div class="perk"><svg width="34" height="26" viewBox="0 0 34 26"><path d="M2 4h18v14H2zM20 9h7l5 5v4H20z" fill="none" stroke="#999" stroke-width="2"/><circle cx="8" cy="21" r="3" fill="#999"/><circle cx="26" cy="21" r="3" fill="#999"/></svg><div>Free Shipping<br>On All Products</div></div>
  <div class="perk"><svg width="32" height="26" viewBox="0 0 32 26"><rect x="1" y="2" width="30" height="18" rx="2" fill="none" stroke="#999" stroke-width="2"/><circle cx="16" cy="11" r="5" fill="#999"/><line x1="1" y1="24" x2="31" y2="24" stroke="#999" stroke-width="2"/></svg><div>Money Back<br>Guarantee</div></div>
  <div class="perk"><svg width="24" height="28" viewBox="0 0 24 28"><rect x="1" y="9" width="22" height="6" fill="#999"/><rect x="3" y="16" width="18" height="11" fill="#999"/><rect x="11" y="9" width="2" height="18" fill="#fff"/><path d="M12 8C8 1 4 4 7 8M12 8c4-7 8-4 5 0" fill="none" stroke="#999" stroke-width="2"/></svg><div>Special Weekly<br>Offer</div></div>
</div>

<nav class="abs nav">
  <div class="nav-home"><svg width="13" height="12" viewBox="0 0 13 12"><path d="M6.5 0L0 6h2v6h3.5V8h2v4H11V6h2z" fill="#fff"/></svg></div>
  <a href="#">ABOUT</a><a href="#">ONLINE STORE</a><a href="#">BLOG</a><a href="#">CONTACTS</a>
  <div class="nav-search"><div class="ico"><svg width="13" height="13" viewBox="0 0 13 13"><circle cx="8" cy="5" r="4" fill="none" stroke="#fff" stroke-width="2"/><line x1="5" y1="8" x2="1" y2="12" stroke="#fff" stroke-width="2.2"/></svg></div><span>Search...</span></div>
</nav>

<!-- hero -->
<section class="abs hero">
  <div class="hero-bg" role="img" aria-label="Soft blurred bokeh photograph of pastel lights"></div>
  <h1 class="hero-title">LOREM IPSUM DOLOR</h1>
  <p class="hero-sub">LOREM IPSUM DOLOR IN INT ORT</p>
  <div class="hero-arrow" style="left:0"><svg width="16" height="32" viewBox="0 0 16 32"><path d="M15 1L1 16l14 15" fill="none" stroke="#777" stroke-width="1.5"/></svg></div>
  <div class="hero-arrow" style="right:0"><svg width="16" height="32" viewBox="0 0 16 32"><path d="M1 1l14 15L1 31" fill="none" stroke="#777" stroke-width="1.5"/></svg></div>
</section>

<!-- promo -->
<div class="abs promo" style="left:75px">
  <div class="promo-kicker">THIS MONTH'S</div>
  <div class="promo-big">MUST<br>HAVE</div>
  <div class="promo-img" role="img" aria-label="Clear quartz and amethyst crystal cluster" style="left:110px;width:140px;background:linear-gradient(135deg,#eeeeee,#dcdce2 50%,#b9a6c6)"></div>
  <div class="promo-info"><div class="promo-name">Lorem ipsum<br>dolor int</div><div class="price">$0.00</div><div class="old">$0.00</div><div style="margin-top:5px"><span class="btn">SHOP NOW</span></div></div>
</div>
<div class="abs promo" style="left:459px">
  <div class="promo-kicker">THIS MONTH'S</div>
  <div class="promo-big">MUST<br>HAVE</div>
  <div class="promo-img" role="img" aria-label="Red hardcover book" style="left:130px;top:22px;width:77px;height:108px;background:linear-gradient(90deg,#4a2a2a 0,#6b2d2d 12%,#b5484a 30%,#b04446)"></div>
  <div class="promo-info"><div class="promo-name">Lorem ipsum<br>dolor int</div><div class="price">$0.00</div><div class="old">$0.00</div><div style="margin-top:5px"><span class="btn">SHOP NOW</span></div></div>
</div>

<!-- new products -->
<h2 class="abs sec-title">NEW PRODUCTS</h2>
<div class="abs sec-rule"></div>

<svg class="abs slide-arrow" style="left:82px" width="12" height="32" viewBox="0 0 12 32"><path d="M11 1L1 16l10 15" fill="none" stroke="#aaa" stroke-width="1.3"/></svg>
<svg class="abs slide-arrow" style="left:806px" width="12" height="32" viewBox="0 0 12 32"><path d="M1 1l10 15L1 31" fill="none" stroke="#777" stroke-width="1.3"/></svg>

<div class="abs card active" style="left:109px">
  <span class="badge">NEW</span>
  <div class="thumb" role="img" aria-label="Quartz and amethyst crystal" style="background:linear-gradient(135deg,#f2f2f2,#dadde2 55%,#b19ac3)"></div>
  <div class="card-name">Lorem ipsum dolor</div><div class="price">$0.00</div><span class="btn">ADD TO CART</span>
</div>
<div class="abs card" style="left:287px">
  <span class="badge">NEW</span>
  <div class="thumb" role="img" aria-label="Red pendulum on a chain" style="background:radial-gradient(ellipse at 50% 65%,#d8302e 0,#e46a66 18%,#fff 40%)"></div>
  <div class="card-name">Lorem ipsum dolor</div><div class="price">$0.00</div><span class="btn">ADD TO CART</span>
</div>
<div class="abs card" style="left:465px">
  <span class="badge">NEW</span>
  <div class="thumb" role="img" aria-label="Stack of coloured books" style="background:linear-gradient(#fff 10%,#e27a78 30%,#c9c1a8 55%,#6f9c9e 80%,#fff 95%)"></div>
  <div class="card-name">Lorem ipsum dolor</div><div class="price">$0.00</div><span class="btn">ADD TO CART</span>
</div>
<div class="abs card" style="left:644px">
  <span class="badge">NEW</span>
  <div class="thumb" role="img" aria-label="Headphones around a stack of CDs" style="background:radial-gradient(ellipse at 50% 55%,#7a8ea8 0,#3c3c44 30%,#fff 55%)"></div>
  <div class="card-name">Lorem ipsum dolor</div><div class="price">$0.00</div><span class="btn">ADD TO CART</span>
</div>

<!-- footer -->
<footer class="abs footer"></footer>

<div class="abs f-col" style="left:75px">
  <div class="f-head">SITEMAP</div>
  <ul class="f-list">
    <li>› Home</li><li class="current">› About</li><li>› Online Store</li><li>› Blog</li><li>› Contacts</li>
  </ul>
</div>

<div class="abs f-col" style="left:333px">
  <div class="f-head">STORE INFORMATION</div>
  <div class="info" style="margin-top:9px">My Company</div>
  <div class="info info-row"><svg width="11" height="14" viewBox="0 0 11 14"><path d="M5.5 0A5 5 0 0 0 .5 5c0 4 5 9 5 9s5-5 5-9a5 5 0 0 0-5-5z" fill="#555"/><circle cx="5.5" cy="5" r="2" fill="#efefef"/></svg><div>00 Lorem ipsum dolor int est<br>Lorem ipsum – 000 00</div></div>
  <div class="info info-row"><svg width="11" height="12" viewBox="0 0 11 12"><path d="M2 0l2 3-1 2c1 2 2 3 3 4l2-1 3 2-2 2C4 11 0 7 0 2z" fill="#555"/></svg><div>Call us now: 0123-456-789</div></div>
  <div class="info info-row"><svg width="12" height="10" viewBox="0 0 12 10"><rect width="12" height="9" y="1" fill="#555"/><path d="M0 1l6 5 6-5" fill="none" stroke="#efefef"/></svg><div>Email: sales@yourcompany.com</div></div>
</div>

<div class="abs f-col" style="left:588px">
  <div class="f-head" style="border:0;padding-bottom:0">FOLLOW US</div>
  <div class="social"><span></span><span></span><span></span></div>
  <div class="f-head" style="margin-top:20px">NEWSLETTER</div>
  <div class="mail"><span>Enter your e-mail</span><span style="color:#555">›</span></div>
  <div class="mail-note">Sign up to receive latest news and updates direct<br>to your inbox.</div>
</div>

<div class="abs copy">© 2014 <b>The Velvet Lantern</b>. All Rights Reserved</div>
<div class="abs pay"><span></span><span></span><span></span><span></span><span></span><span></span></div>

</body>
</html>
```